Web-site design for company trading in chemicals & lubricants

We need a standard 5 page web-site designed for our company based in Dubai, UAE.
The web-site should highlight our capacity to store material as well as distribute the same. The products we sell are basic chemicals - packed in bags as well as drums. Bags are big bags - 25 kgs each as well as drums - 200 litres each. We want to highlight the fact that we huge stocks of this material & can deliver by sea & road,
Please use this site as a ref - http://www.brivex-solvents.co.uk/
Besides this, we need a page dedicated to finished products that we are selling for use in the auto industry - lubricants, motor oils,brake-fluids, greases, coolants etc. This are packed in large drums as well as small cans.
It would be nice if the site could immediately also provide a ref. to our location - Dubai or that we are based in the Middle East.
We will provide our company logo for reference

```html
<!DOCTYPE html>
<html lang="en">
<head>
<meta charset="utf-8">
<title>VARENTIS — Industrial Chemicals &amp; Lubricants</title>
<link href="https://fonts.googleapis.com/css2?family=Roboto:wght@300;400&family=Roboto+Condensed:wght@400;700&family=Noto+Sans:wght@400&display=swap" rel="stylesheet">
<style>
:root{
  --brown:#4b2c17;
  --olive:#8c7416;
  --olive-dark:#7a6405;
  --gold-light:#c9a93a;
  --ink:#1d1d1d;
  --grey-text:#5a5f66;
  --panel-top:#f4f7fb;
  --panel-bottom:#dfe6ef;
  --panel-border:#cdd6e1;
  --footer-bg:#e2eaf3;
  --sky-top:#cfdeee;
}
*{margin:0;padding:0;box-sizing:border-box}
html,body{width:1106px;height:1200px;overflow:hidden}
body{
  position:relative;
  background:linear-gradient(180deg,var(--sky-top) 0,#f2f6fb 140px,#fff 420px,#fff 1009px);
  font-family:"Noto Sans",sans-serif;color:var(--ink);
}
.top-rule{position:absolute;left:0;top:0;width:100%;height:5px;background:var(--brown)}
.brand{position:absolute;left:57px;top:48px;display:flex;align-items:center;gap:12px}
.brand-name{font-family:"Roboto Condensed",sans-serif;font-weight:700;font-size:46px;letter-spacing:2px;color:var(--brown);line-height:1}
.brand-dot{width:22px;height:22px;border-radius:50%;background:var(--olive)}
.phone{position:absolute;right:61px;top:52px;font-family:"Roboto",sans-serif;font-weight:300;font-size:26px;color:var(--olive)}
.main-nav{position:absolute;right:61px;top:88px;display:flex;gap:6px}
.main-nav a{font-family:"Roboto Condensed",sans-serif;font-size:17px;color:var(--gold-light);text-decoration:none;padding:5px 8px;height:32px;line-height:22px}
.main-nav a.active{background:var(--olive-dark);color:#fff}
.hero{position:absolute;left:55px;top:134px;width:990px;height:298px;border-radius:6px;overflow:hidden;
  box-shadow:0 2px 6px rgba(0,0,0,.25)}
.hero-photo{position:absolute;inset:0;background:linear-gradient(180deg,#7d8ea5 0,#a7b6c6 40%,#c9ced4 65%,#8e9299 100%)}
.hero-title{position:absolute;left:27px;top:30px;font-family:"Roboto",sans-serif;font-weight:300;font-size:29px;line-height:35px;color:#fff}
.hero-cta{position:absolute;left:27px;top:107px;width:174px;height:38px;border-radius:4px;
  background:linear-gradient(180deg,#c8a73c,#8c6d0a);display:flex;align-items:center;padding-left:16px;gap:10px;
  font-family:"Roboto Condensed",sans-serif;font-size:19px;letter-spacing:1px;color:#fff}
.welcome{position:absolute;left:55px;top:458px;width:492px}
.section-title{font-family:"Roboto Condensed",sans-serif;font-size:20px;color:#4a4f55;font-weight:400}
.section-title span{color:var(--olive)}
.welcome .section-title{padding-bottom:8px;border-bottom:1px dashed #b9bec4}
.welcome p{margin-top:8px;font-size:12.5px;line-height:17px;letter-spacing:.6px}
.ticks{list-style:none;margin-top:16px}
.ticks li{font-size:12.5px;line-height:20px;letter-spacing:.6px;display:flex;align-items:center;gap:6px}
.panel{position:absolute;border:1px solid var(--panel-border);border-radius:6px;background:linear-gradient(180deg,var(--panel-top),var(--panel-bottom))}
.panel .section-title{color:var(--olive)}
.partners{left:588px;top:462px;width:457px;height:209px;padding:12px 8px}
.partner-grid{display:grid;grid-template-columns:repeat(3,1fr);gap:20px 18px;margin-top:8px;padding:0 10px}
.partner-badge{height:60px;border-radius:4px;background:#c3c9d1}
.news{left:55px;top:738px;width:237px;height:209px;padding:12px 8px}
.news-item{display:flex;gap:11px;margin-top:10px;font-size:12.5px;line-height:17px;letter-spacing:.6px}
.news-item:first-of-type{margin-top:12px}
.news-item + .news-item{margin-top:19px}
.news-thumb{width:37px;height:37px;background:#000;flex:none;margin-top:3px}
.sector{position:absolute;top:740px;width:208px}
.sector-photo{height:112px;border-radius:6px;box-shadow:0 6px 8px -4px rgba(0,0,0,.25)}
.sector h3{margin-top:20px;font-family:"Roboto Condensed",sans-serif;font-weight:400;font-size:20px;letter-spacing:.5px;color:var(--olive)}
.sector p{margin-top:4px;font-size:12.5px;line-height:17px;letter-spacing:.6px;text-align:justify}
.sector a{color:var(--olive-dark)}
.site-footer{position:absolute;left:0;top:1009px;width:100%;height:191px;background:var(--footer-bg)}
.foot-col{position:absolute;top:8px}
.foot-col h4{font-weight:400;font-size:12.5px;letter-spacing:.8px;color:#666;margin-bottom:10px}
.foot-col a{display:block;font-size:11px;line-height:18px;letter-spacing:.4px;color:#111;text-decoration:none}
.copyright{position:absolute;left:246px;top:122px;font-size:11px;letter-spacing:.4px}
.address{position:absolute;right:68px;top:6px;text-align:right;font-size:11px;line-height:18px;letter-spacing:.4px}
</style>
</head>
<body>
<div class="top-rule"></div>
<header>
  <div class="brand"><span class="brand-name">VARENTIS</span><span class="brand-dot"></span></div>
  <div class="phone">Call: +971-4-555 0142</div>
  <nav class="main-nav">
    <a class="active" href="#">Home</a><a href="#">Abouts Us</a><a href="#">Partners</a><a href="#">Logistic</a><a href="#">News</a><a href="#">Contact Us</a>
  </nav>
</header>

<section class="hero">
  <div class="hero-photo" role="img" aria-label="Spherical storage tanks and refinery towers under a cloudy sky"></div>
  <h1 class="hero-title">Sharing knowledge and providing solutions<br>for the industrial chemical industry</h1>
  <a class="hero-cta">CONTACT US
    <svg width="22" height="22" viewBox="0 0 22 22"><circle cx="11" cy="11" r="10" fill="#fff"/><path d="M8 6l7 5-7 5z" fill="#6b5406"/></svg>
  </a>
</section>

<section class="welcome">
  <h2 class="section-title">Welcome to <span>VARENTIS</span></h2>
  <p>Vivamus vel orci arcu. Curabitur laoreet dolor nec nunc porta non aliquam lorem ultricies. Etiam eget mi lectus, ac lacinia sapien. Donec a arcu id lectus sodales consectetur.</p>
  <ul class="ticks">
    <li><svg width="12" height="11" viewBox="0 0 12 11"><path d="M1 6l3 4 7-9" stroke="#c9a22e" stroke-width="2.4" fill="none"/></svg>Sed convallis tincidunt purus, ut varius metus ultrices non.</li>
    <li><svg width="12" height="11" viewBox="0 0 12 11"><path d="M1 6l3 4 7-9" stroke="#c9a22e" stroke-width="2.4" fill="none"/></svg>Ut faucibus purus vitae nisi varius vel interdum diam faucibus.</li>
    <li><svg width="12" height="11" viewBox="0 0 12 11"><path d="M1 6l3 4 7-9" stroke="#c9a22e" stroke-width="2.4" fill="none"/></svg>Curabitur luctus urna vel risus tristique faucibus.</li>
    <li><svg width="12" height="11" viewBox="0 0 12 11"><path d="M1 6l3 4 7-9" stroke="#c9a22e" stroke-width="2.4" fill="none"/></svg>Duis ultricies porta urna, vitae luctus risus malesuada et.</li>
  </ul>
</section>

<aside class="panel partners">
  <h2 class="section-title">Partners</h2>
  <div class="partner-grid">
    <div class="partner-badge"></div><div class="partner-badge"></div><div class="partner-badge"></div>
    <div class="partner-badge"></div><div class="partner-badge"></div><div class="partner-badge"></div>
  </div>
</aside>

<aside class="panel news">
  <h2 class="section-title">News</h2>
  <div class="news-item"><span class="news-thumb"></span><span>Curabitur laoreet dolor nec nunc porta.</span></div>
  <div class="news-item"><span class="news-thumb"></span><span>Curabitur laoreet dolor nec nunc porta.</span></div>
  <div class="news-item"><span class="news-thumb"></span><span>Curabitur laoreet dolor nec nunc porta.</span></div>
</aside>

<article class="sector" style="left:330px">
  <div class="sector-photo" role="img" aria-label="Industrial plant with cooling towers releasing steam" style="background:linear-gradient(180deg,#3f6fb0,#9fb7d4 55%,#6c6f72)"></div>
  <h3>INDUSTRIAL</h3>
  <p>Vivamus vel orci arcu. Curabitur laoreet dolor nec nunc ... <a href="#">continue reading</a></p>
</article>
<article class="sector" style="left:584px">
  <div class="sector-photo" role="img" aria-label="Hand truck stacked with cardboard boxes beside a globe" style="background:linear-gradient(135deg,#f4f4f2,#e2c48e 55%,#c79a5a)"></div>
  <h3>PACKAGING</h3>
  <p>Vivamus vel orci arcu. Curabitur laoreet dolor nec nunc...<a href="#">continue reading</a></p>
</article>
<article class="sector" style="left:837px">
  <div class="sector-photo" role="img" aria-label="Mechanic working on a car engine with a wrench" style="background:linear-gradient(160deg,#2d3036,#5b6068 50%,#1e2024)"></div>
  <h3>AUTOMOBILE</h3>
  <p>Vivamus vel orci arcu. Curabitur laoreet dolor nec nunc...<a href="#">continue reading</a></p>
</article>

<footer class="site-footer">
  <div class="foot-col" style="left:57px"><h4>Main Navigation</h4>
    <a href="#">Home</a><a href="#">About Us</a><a href="#">Partners</a><a href="#">Logistic</a><a href="#">News</a><a href="#">Contact Us</a></div>
  <div class="foot-col" style="left:245px"><h4>Info</h4>
    <a href="#">Terms of Use</a><a href="#">Privacy Policy</a></div>
  <div class="foot-col" style="left:415px"><h4>Other</h4>
    <a href="#">Industrial</a><a href="#">Packaging</a><a href="#">Automobile</a></div>
  <div class="copyright">Copyright 2011 © VARENTIS. All Rights Reserved.</div>
  <address class="address" style="font-style:normal">Creekside Trade House<br>Harbour Street, Deira<br>P.O. Box 2280 – Dubai, U.A.E<br><br>p:123-456-7890<br>f:123-456-7897</address>
</footer>
</body>
</html>
```